Harbourview Motor Works Business Card Design

Looking for a "clean and sharp" looking business card. Really like the design in the attachment? Our colours are black, white and red. Would like to see the curves with some metallic/shimmer colour and wouldn't mind if the front background was high gloss black.

Target Market(s)

Car owners

Industry/Entity Type

Business

Contact Information for Business Card

On the front:
Harbourview Motor Works
ABN 731 902 514 67
48 Brenton Parade
Tewantin Q 4539
Phone: 07 5418 9276
On the back:
General Servicing
Timing Belts
Brake Repairs
Injector Servicing
Suspension
Log Book Servicing
Clutches
Email: harbourviewmotorworks@mailbox-example.com
All work guaranteed by Qualified Master Mechanic 20 years experience

Colors
ffffff
ec1f27
000000

Requirements
Must have
• Must have the curved lines above the text in some type of metallic

```html
<!DOCTYPE html>
<html lang="en">
<head>
<meta charset="utf-8">
<title>Harbourview Motor Works – Business Card</title>
<link href="https://fonts.googleapis.com/css2?family=Open+Sans:ital,wght@0,400;0,600;0,700;1,700;1,800&display=swap" rel="stylesheet">
<style>
  :root {
    --card-black: #000000;
    --card-gloss: #141414;
    --ink-white: #ffffff;
    --brand-red: #ec1f27;
    --deep-red: #a3151b;
    --page-bg: #e6e3df;
    --rule-silver: #b9b9b9;
    --sheen-red: rgba(236, 31, 39, 0.55);
    --sheen-silver: rgba(220, 220, 220, 0.35);
  }
  * { margin: 0; padding: 0; box-sizing: border-box; }
  html, body { width: 1200px; height: 1000px; overflow: hidden; }
  body {
    background: var(--page-bg);
    font-family: "Open Sans", Arial, sans-serif;
    color: var(--ink-white);
    position: relative;
  }
  .card {
    position: absolute;
    left: 220px;
    width: 760px;
    height: 450px;
    border-radius: 34px;
    background: radial-gradient(ellipse at 40% 25%, var(--card-gloss) 0%, var(--card-black) 70%);
    box-shadow: 0 10px 28px rgba(0,0,0,0.28);
    overflow: hidden;
  }
  .card--front { top: 35px; }
  .card--back { top: 515px; }

  /* metallic curve motif areas */
  .sheen {
    position: absolute;
    border-radius: 50%;
  }
  .sheen--front {
    left: 170px; top: 78px; width: 470px; height: 80px;
    background: radial-gradient(ellipse at 40% 60%, var(--sheen-silver) 0%, var(--sheen-red) 35%, rgba(0,0,0,0) 70%);
    opacity: 0.55;
  }
  .sheen--back {
    left: 90px; top: 40px; width: 600px; height: 130px;
    background: radial-gradient(ellipse at 45% 45%, var(--sheen-silver) 0%, rgba(120,120,120,0.18) 40%, rgba(0,0,0,0) 70%);
  }

  /* front */
  .brand {
    position: absolute;
    left: 170px;
    top: 160px;
    display: flex;
    align-items: center;
    gap: 12px;
  }
  .brand__dot {
    width: 12px; height: 12px;
    border-radius: 50%;
    background: var(--brand-red);
  }
  .brand__name {
    font-size: 33px;
    font-weight: 700;
    color: var(--ink-white);
    line-height: 1;
  }
  .rule {
    position: absolute;
    height: 2px;
    background: linear-gradient(90deg, var(--rule-silver), #ffffff 45%, #555555);
  }
  .rule--front { left: 170px; top: 212px; width: 480px; }
  .rule--back { left: 40px; top: 180px; width: 680px; }

  .legal {
    position: absolute;
    right: 52px;
    top: 250px;
    text-align: right;
    font-size: 18px;
    line-height: 30px;
  }
  .legal__label { color: var(--brand-red); }

  .contact {
    position: absolute;
    left: 42px;
    top: 362px;
    font-size: 17px;
    line-height: 30px;
    list-style: none;
  }
  .contact li { display: flex; align-items: center; gap: 10px; }
  .contact svg { width: 14px; height: 14px; flex: none; }

  /* back */
  .services {
    position: absolute;
    list-style: none;
    font-size: 20px;
    line-height: 29px;
  }
  .services li { display: flex; align-items: center; gap: 8px; }
  .services li::before {
    content: "";
    width: 8px; height: 8px;
    border-radius: 50%;
    background: var(--deep-red);
    flex: none;
  }
  .services--left { left: 40px; top: 212px; }
  .services--middle { left: 280px; top: 250px; }
  .services--right { right: 44px; top: 305px; }
  .services--right li { justify-content: flex-end; }

  .guarantee {
    position: absolute;
    left: 40px;
    right: 40px;
    top: 398px;
    font-size: 19.5px;
    font-weight: 800;
    font-style: italic;
    color: var(--deep-red);
    white-space: nowrap;
  }
</style>
</head>
<body>

<section class="card card--front" aria-label="Business card front">
  <div class="sheen sheen--front" role="img" aria-label="Metallic red and silver curved lines above the business name"></div>
  <div class="brand">
    <span class="brand__dot"></span>
    <span class="brand__name">Harbourview Motor Works</span>
  </div>
  <div class="rule rule--front"></div>

  <p class="legal">
    <span class="legal__label">ABN</span> 731 902 514 67<br>
    48 Brenton Parade Tewantin Q 4539
  </p>

  <ul class="contact">
    <li>
      <svg viewBox="0 0 14 14" aria-hidden="true"><rect x="3.5" y="1" width="7" height="12" rx="1.3" fill="none" stroke="#ec1f27" stroke-width="1.4"/></svg>
      07 5418 9276
    </li>
    <li>
      <svg viewBox="0 0 14 14" aria-hidden="true"><rect x="1" y="3" width="12" height="8" fill="none" stroke="#ec1f27" stroke-width="1.4"/><path d="M1 3 L7 8 L13 3" fill="none" stroke="#ec1f27" stroke-width="1.4"/></svg>
      harbourviewmotorworks@mailbox-example.com
    </li>
  </ul>
</section>

<section class="card card--back" aria-label="Business card back">
  <div class="sheen sheen--back" role="img" aria-label="Large faint silver metallic curved lines"></div>
  <div class="rule rule--back"></div>

  <ul class="services services--left">
    <li>General Servicing</li>
    <li>Timing Belts</li>
  </ul>
  <ul class="services services--middle">
    <li>Brake Repairs</li>
    <li>Injector Servicing</li>
    <li>Suspension</li>
  </ul>
  <ul class="services services--right">
    <li>Log Book Servicing</li>
    <li>Clutches</li>
  </ul>

  <p class="guarantee">All work guaranteed by Qualified Master Mechanic 20 years experience</p>
</section>

</body>
</html>
```